Brovane Grand Opening

I need a one sided flyer that advertises my grand opening for our new equipment dealership.

Grand Opening

New and Used Equipment Sales
Equipment Rentals
Residential, Commercial and Industrial Rental Equipment
Construction and Industrial Supply
Custom Metal Fabrication
Mobile Welding Service
Pickup and Delivery Service
24hr. Emergency Dedicated Service

Now Open!

4362 Marlowfield HWY
Easley, SC 29640

(555) 318 - 4026

7:00am-7:00pm Monday - Friday
8:00am-3:00pm Saturday

www.brovanegear.example

```html
<!DOCTYPE html>
<html lang="en">
<head>
<meta charset="utf-8">
<title>Brovane Grand Opening</title>
<link href="https://fonts.googleapis.com/css2?family=Anton&family=Saira+Semi+Condensed:wght@500;600;700;800&display=swap" rel="stylesheet">
<style>
  :root {
    --page: #d4d4d4;
    --ink: #1b1a1b;
    --deep: #120c0d;
    --wine: #5a0b10;
    --red: #e3202a;
    --red-dark: #b3121b;
    --white: #ffffff;
    --pale: #e9e9e9;
    --gold-light: #f3ecc4;
    --gold: #c9a94a;
    --gold-dark: #6e5818;
  }
  * { margin: 0; padding: 0; box-sizing: border-box; }
  html, body { width: 1136px; height: 1200px; overflow: hidden; }
  body {
    background: var(--page);
    font-family: "Saira Semi Condensed", "Arial Narrow", sans-serif;
    color: var(--white);
  }
  .flyer {
    position: absolute; left: 143px; top: 0;
    width: 850px; height: 1200px; overflow: hidden;
    background:
      radial-gradient(ellipse 70% 30% at 50% 40%, rgba(150,18,28,.7), transparent 70%),
      linear-gradient(180deg, #1e1c1d 0%, #2a1416 18%, var(--wine) 40%, #3a0b0e 58%, #1c0c0d 72%, var(--deep) 76%);
  }

  .brand {
    position: absolute; top: 49px; left: 0; width: 100%; height: 58px;
    display: flex; justify-content: center; align-items: center; gap: 14px;
    white-space: nowrap;
  }
  .brand-mark { width: 32px; height: 32px; background: var(--red); }
  .brand-name { font-weight: 800; font-size: 74px; line-height: 58px; color: var(--white); }

  .headline {
    position: absolute; left: 0; width: 100%; text-align: center; white-space: nowrap;
    font-family: "Anton", Impact, sans-serif; font-weight: 400; line-height: 1;
    -webkit-background-clip: text; background-clip: text; color: transparent;
    filter: drop-shadow(0 4px 6px rgba(0,0,0,.7));
  }
  .headline-grand {
    top: 139px; font-size: 182px; letter-spacing: 12px; padding-left: 12px;
    background-image: linear-gradient(180deg, var(--gold-light) 0%, var(--gold) 45%, var(--gold-dark) 60%, var(--gold) 100%);
  }
  .headline-opening {
    top: 318px; font-size: 182px; letter-spacing: 11px; padding-left: 11px;
    background-image: linear-gradient(180deg, #ffffff 0%, #cfcfcf 40%, #7c7c7c 55%, #f2f2f2 80%, #9a9a9a 100%);
  }

  .services {
    position: absolute; left: 70px; top: 556px; width: 709px; height: 203px;
    border: 1.5px dashed var(--red); border-radius: 6px;
  }
  .services-label {
    position: absolute; top: -23px; left: 50%; transform: translateX(-50%);
    background: var(--red); border-radius: 10px; padding: 0 12px;
    font-weight: 700; font-size: 29px; line-height: 38px; white-space: nowrap;
  }
  .services-list {
    position: absolute; top: 29px; list-style: none; white-space: nowrap;
    font-weight: 600; font-size: 21px; line-height: 26px;
  }
  .services-list.left { left: 42px; }
  .services-list.right { left: 428px; }
  .services-list li { position: relative; margin-bottom: 8px; }
  .services-list li::before {
    content: ""; position: absolute; left: -27px; top: 6px;
    width: 7px; height: 13px;
    border-right: 3px solid var(--red); border-bottom: 3px solid var(--red);
    transform: rotate(40deg);
  }

  .now-open {
    position: absolute; left: 70px; top: 801px; width: 270px; height: 78px;
    background: linear-gradient(180deg, var(--red), var(--red-dark));
    border-radius: 8px; text-align: center; white-space: nowrap;
    font-family: "Anton", Impact, sans-serif; font-size: 56px; line-height: 78px;
  }
  .hours {
    position: absolute; left: 340px; top: 801px; width: 448px; height: 78px;
    background: rgba(0,0,0,.55);
    display: grid; grid-template-columns: 217px 38px auto; align-content: center;
    font-weight: 700; font-size: 24px; line-height: 30px; white-space: nowrap;
  }
  .hours .day { text-align: right; color: var(--pale); }
  .hours .arrow { text-align: center; color: var(--red); }
  .hours .time { color: var(--red); }

  .equipment-strip { position: absolute; left: 0; top: 910px; width: 850px; height: 156px; display: block; }

  .contact {
    position: absolute; left: 0; top: 1066px; width: 850px; height: 134px;
    background: var(--ink);
  }
  .call-line { position: absolute; left: 88px; top: 41px; width: 673px; height: 3px; background: var(--red); }
  .call-bar {
    position: absolute; left: 168px; top: 20px; width: 512px; height: 47px;
    background: var(--red); clip-path: polygon(3% 0, 100% 0, 97% 100%, 0 100%);
    display: flex; justify-content: center; align-items: center; gap: 10px;
    white-space: nowrap; font-weight: 800; font-size: 32px; line-height: 47px;
  }
  .call-bar svg { flex: none; }
  .contact-details {
    position: absolute; left: 0; top: 80px; width: 100%; height: 30px;
    display: flex; justify-content: center; align-items: center; gap: 26px;
    white-space: nowrap; font-weight: 600; font-size: 20px; line-height: 30px;
  }
  .detail { display: flex; align-items: center; gap: 8px; }
  .detail svg { flex: none; }
  .web-name { color: var(--red); }
</style>
</head>
<body>
<main class="flyer">
  <div class="brand">
    <span class="brand-mark"></span>
    <span class="brand-name">BROVANE</span>
  </div>

  <h1 class="headline headline-grand">GRAND</h1>
  <h1 class="headline headline-opening">OPENING</h1>

  <section class="services">
    <h2 class="services-label">WE PROVIDE YOU</h2>
    <ul class="services-list left">
      <li>New and Used Equipment Sales</li>
      <li>Equipment Rentals</li>
      <li>Residential, Commercial and<br>Industrial Rental Equipment</li>
      <li>Construction and Industrial Supply</li>
    </ul>
    <ul class="services-list right">
      <li>Custom Metal Fabrication</li>
      <li>Mobile Welding Service</li>
      <li>Pickup and Delivery Service</li>
      <li>24hr. Emergency Dedicated<br>Service</li>
    </ul>
  </section>

  <div class="now-open">NOW OPEN!</div>
  <div class="hours">
    <span class="day">MONDAY - FRIDAY</span><span class="arrow">&gt;</span><span class="time">7:00AM-7:00PM</span>
    <span class="day">SATURDAY</span><span class="arrow">&gt;</span><span class="time">8:00AM-3:00PM</span>
  </div>

  <svg class="equipment-strip" viewBox="0 0 850 156" width="850" height="156">
    <defs>
      <linearGradient id="excavator" x1="0" y1="0" x2="0" y2="1"><stop offset="0" stop-color="#8fa9c4"/><stop offset=".6" stop-color="#d9a21c"/><stop offset="1" stop-color="#8a7a66"/></linearGradient>
      <linearGradient id="tractor" x1="0" y1="0" x2="0" y2="1"><stop offset="0" stop-color="#aab3a8"/><stop offset=".45" stop-color="#2f9e33"/><stop offset="1" stop-color="#1d5e22"/></linearGradient>
      <linearGradient id="crawler" x1="0" y1="0" x2="0" y2="1"><stop offset="0" stop-color="#c86a3a"/><stop offset=".5" stop-color="#5b5b58"/><stop offset="1" stop-color="#8c8c88"/></linearGradient>
      <linearGradient id="harvester" x1="0" y1="0" x2="0" y2="1"><stop offset="0" stop-color="#7c8a6e"/><stop offset=".6" stop-color="#6e6a5c"/><stop offset="1" stop-color="#9a8f7c"/></linearGradient>
    </defs>
    <rect width="850" height="156" fill="#111"/>
    <polygon points="0,0 20,0 0,90" fill="#e3202a"/>
    <polygon points="22,0 237,0 202,156 0,156 0,100" fill="url(#excavator)" role="img" aria-label="Yellow excavator working a gravel pile"/>
    <polygon points="245,0 443,0 408,156 210,156" fill="url(#tractor)" role="img" aria-label="Row of green farm tractors"/>
    <polygon points="451,0 650,0 615,156 416,156" fill="url(#crawler)" role="img" aria-label="Orange crawler excavator loaded on a trailer"/>
    <polygon points="658,0 850,0 850,60 828,156 623,156" fill="url(#harvester)" role="img" aria-label="Forestry harvester cutting a log in the woods"/>
    <polygon points="850,66 850,156 830,156" fill="#e3202a"/>
  </svg>

  <footer class="contact">
    <div class="call-line"></div>
    <div class="call-bar">
      <svg width="24" height="24" viewBox="0 0 24 24" aria-hidden="true">
        <rect width="24" height="24" rx="5" fill="#fff"/>
        <path d="M6 5 q2 -1 3 1 l1 3 q0 2 -2 2 q1 4 5 6 q0 -2 2 -2 l3 1 q2 1 1 3 q-2 3 -6 1 q-7 -4 -8 -11 q0 -3 1 -4z" fill="#e3202a"/>
      </svg>
      <span>CALL NOW:&nbsp; (555) 318 - 4026</span>
    </div>
    <div class="contact-details">
      <span class="detail">
        <svg width="16" height="21" viewBox="0 0 16 21" aria-hidden="true">
          <path d="M8 0 a8 8 0 0 1 8 8 c0 6 -8 13 -8 13 s-8 -7 -8 -13 a8 8 0 0 1 8 -8z" fill="#e3202a"/>
          <circle cx="8" cy="8" r="3" fill="#1b1a1b"/>
        </svg>
        4362 Marlowfield HWY, Easley, SC 29640
      </span>
      <span class="detail">
        <svg width="18" height="18" viewBox="0 0 18 18" aria-hidden="true">
          <circle cx="9" cy="9" r="9" fill="#e3202a"/>
          <path d="M0 9 h18 M9 0 v18 M3 3 q6 6 12 0 M3 15 q6 -6 12 0" stroke="#1b1a1b" stroke-width="1.4" fill="none"/>
        </svg>
        <span>www.<span class="web-name">brovanegear</span>.example</span>
      </span>
    </div>
  </footer>
</main>
</body>
</html>
```